New Agency Branding - Logo & Business Card

Project Description

ZIP is a creative agency that crafts memorable product experiences through meaningful design. By channeling the needs of the business and its customers, we are able to construct solutions that are elegant yet effective, powerful yet playful, and familiar yet stimulating.

In addition to our focus towards creating excellent products, we firmly believe that building a strong company culture is paramount. Our values revolve around building an environment that is passionate, supportive, collaborative, curious, humorous, and healthy. The ZIP team is relatively small, and we intend on keep this family tight-knit. We take great care in deciding who we work with and what we work on.

What we’re looking for is a designer who is willing to take on the challenge of helping us visually define and express the ZIP brand. We must comfortably occupy the consumer, commercial, and enterprise sectors. This means looking professional without sacrificing charm. We’re passionate about design and we care about people.

Deliverables

Logo

The first exercise would be to create the ZIP logo by referencing the concept that is attached (filename: ZIP Concept Logo). We like the idea of utilizing negative space, but are open to other suggestions. In terms of color, we’ve been flirting with the idea of purple as the primary color, but are again open to other explorations. The logo should be bold, professional, playful, and versatile (it should look just as crisp blown up on a website as it would on a contract).

Accepted Format(s): Adobe Illustrator (.ai) 

Business Card

The second exercise would be to design a business card utilizing the logo. The shape can be standard or square (single our double-sided), and must include the following:

• ZIP Logo
• Tagline: "Thoughtful products, Crafted"
• First and Last Name
• Job Role
• Contact Information (email address and phone number)
• Website URL

In terms of typography, we’d like to see considered pairings that compliment the logo, are legible, and can cohesively translate to other mediums (i.e. the ZIP website).

Accepted Format(s): Adobe Photoshop (.psd) OR Adobe Illustrator (.ai)

Style Guide

Finally, we’d like to have the brand defined and presented in a style guide. This would include the full color palette (primary color, secondary color, etc.) and font usage. In addition, we’d like to see rationale clearly communicated for the decisions made.

Visual References

Companies that inspire us:

morrow+finch
http://www.morrowfinch.example/story/morrow-finch/

BRISK
http://www.briskco.example

NestLoop
https://www.nestloop.example

Fundwheel
https://www.fundwheel.example

Target Market(s)

Startups, Small to Mid Sized Businesses, Consultant Businesses

Industry/Entity Type

Design Agency

Contact Information for Business Card

FRONT: ZIP LOGO on White background

BACK: Tag line "Thoughtful products, Crafted", name (i.e. Mark Ellery), job role (i.e. Director, Product Development), phone number, email address, and website. The background color could be a solid color although we are open to suggestions.

Logo Text

ZIP

Font styles to use
Sans Serif

Colors
b768aa
a54499
d2a4cc
876aae
6b449b

Requirements
Must have
• A sense of playfulnesses, charm, excitement, and energy.
• Clean and minimal design
• Avoid using icons for contact information
• NOTE: Not all of the purples that have been chosen must be used. These are only suggestions.

```html
<!DOCTYPE html>
<html lang="en">
<head>
<meta charset="utf-8">
<title>ZIP — Business Card</title>
<link rel="stylesheet" href="https://fonts.googleapis.com/css2?family=Source+Sans+3:wght@400;600&display=swap">
<style>
  :root {
    --page-bg: #141414;
    --card-white: #f3f3f3;
    --brand-purple: #876aae;
    --brand-purple-deep: #7a5ca6;
    --brand-purple-emboss: #7d60a6;
    --text-grey: #5a5a5a;
  }
  html, body {
    margin: 0;
    padding: 0;
    width: 1200px;
    height: 900px;
    overflow: hidden;
    background: var(--page-bg);
    font-family: "Source Sans 3", "Myriad Pro", Arial, sans-serif;
  }
  .canvas {
    position: relative;
    width: 1200px;
    height: 900px;
  }
  .card {
    position: absolute;
    top: 184px;
    height: 490px;
    border-radius: 12px;
    box-sizing: border-box;
  }
  .card--front {
    left: 299px;
    width: 301px;
    background: var(--card-white);
    text-align: center;
  }
  .card--back {
    left: 645px;
    width: 304px;
    background: var(--brand-purple);
  }
  .wordmark {
    position: absolute;
    left: 0;
    right: 0;
    margin: 0;
    font-weight: 600;
    line-height: 1;
    text-align: center;
    letter-spacing: 4px;
  }
  .card--front .wordmark {
    top: 62px;
    font-size: 128px;
    color: var(--brand-purple);
  }
  .card--back .wordmark {
    top: 184px;
    font-size: 132px;
    color: var(--brand-purple-emboss);
  }
  .tagline {
    position: absolute;
    top: 211px;
    left: 0;
    right: 0;
    margin: 0;
    font-size: 16px;
    color: var(--brand-purple-deep);
  }
  .contact {
    position: absolute;
    top: 274px;
    left: 0;
    right: 0;
    color: var(--text-grey);
    font-size: 14px;
    line-height: 17.5px;
  }
  .contact__name {
    margin: 0;
    font-size: 17px;
    font-weight: 600;
    line-height: 20px;
    color: var(--brand-purple-deep);
  }
  .contact__role { margin: 0 0 12px; }
  .contact__address { margin: 0 0 14px; font-style: normal; }
  .contact__lines { margin: 0; }
</style>
</head>
<body>
  <main class="canvas">
    <section class="card card--front" aria-label="Business card front">
      <p class="wordmark">ZIP</p>
      <p class="tagline">Thoughtful products, Crafted</p>
      <div class="contact">
        <p class="contact__name">Daniel Carver</p>
        <p class="contact__role">Managing Director</p>
        <address class="contact__address">12345, Address Goes Here<br>Country Name, 123456.</address>
        <p class="contact__lines">044-555 010 234<br>info@zipstudio.example<br>www.zipstudio.example</p>
      </div>
    </section>
    <section class="card card--back" aria-label="Business card back">
      <p class="wordmark">ZIP</p>
    </section>
  </main>
</body>
</html>
```